Point of sale box designs , I have templets.

I need point of sale box design according to my requirements.
I have all files at the ready. Each windows file has a;; the information you will need.
see files I uploded.
This project is 90% cut and paste. look into all the windows files for instructions ,text, bar codes and there placement.
You only have to draw the 3 steps on how to use the product.
Industry/Entity Type
General consumer product.
Nice to have
- Taxi cab yellow background with black text.

```html
<!DOCTYPE html>
<html lang="en">
<head>
<meta charset="utf-8">
<title>Sauce Sachet Snipper – Point of Sale Box Dielines</title>
<link href="https://fonts.googleapis.com/css2?family=Arimo:wght@400;700&family=Tinos&family=Titillium+Web:wght@400;600&display=swap" rel="stylesheet">
<style>
  :root {
    --cab-yellow: #ffcb05;
    --ink: #111111;
    --paper: #ffffff;
    --cut-orange: #e8a200;
    --cut-blue: #3b3b9c;
    --dim-green: #5fb08e;
    --dim-blue: #3b3b9c;
    --icon-tone: #e0a900;
  }
  html, body { margin: 0; padding: 0; overflow: hidden; background: var(--paper); }
  .sheet { display: block; width: 1200px; height: 1032px; }
  .panel { fill: var(--cab-yellow); }
  .die-top .panel { stroke: var(--cut-orange); stroke-width: 1.2; }
  .die-bottom .panel { stroke: var(--cut-blue); stroke-width: 1.2; }
  .fold { stroke: var(--cut-blue); stroke-width: 1; fill: none; }
  .fold-orange { stroke: var(--cut-orange); stroke-width: 1; fill: none; stroke-dasharray: 3 2; }
  .code-slot { fill: var(--paper); }
  .box-text { font-family: "Arimo", Arial, sans-serif; font-weight: 700; fill: var(--ink); }
  .mid { text-anchor: middle; }
  .end { text-anchor: end; }
  .step-tag { fill: var(--ink); }
  .step-tag-text { font-family: "Arimo", Arial, sans-serif; font-weight: 700; fill: var(--cab-yellow); text-anchor: middle; }
  .step-art { fill: var(--icon-tone); }
  .mark-ring { fill: none; stroke: var(--ink); stroke-width: 1.2; }
  .card-text { font-family: "Titillium Web", Arial, sans-serif; fill: var(--ink); }
  .card-bold { font-weight: 600; }
  .pill { fill: var(--ink); }
  .pill-text { font-family: "Titillium Web", Arial, sans-serif; fill: var(--paper); text-anchor: middle; font-size: 16px; }
  .pill-dot { fill: var(--paper); }
  .punch-frame { fill: none; stroke: var(--ink); stroke-width: 2; }
  .dim-green { stroke: var(--dim-green); stroke-width: 1.2; fill: none; }
  .dim-blue { stroke: var(--dim-blue); stroke-width: 1.2; fill: none; }
  .dim-sans { font-family: "Arimo", Arial, sans-serif; fill: #222; text-anchor: middle; }
  .dim-serif { font-family: "Tinos", "Times New Roman", serif; fill: #222; text-anchor: middle; }
</style>
</head>
<body>
<svg class="sheet" viewBox="0 0 2048 1762" xmlns="http://www.w3.org/2000/svg" xmlns:xlink="http://www.w3.org/1999/xlink">
  <defs>
    <!-- large three-step instructions, panel origin at top-left -->
    <g id="steps-large">
      <rect class="step-tag" x="28" y="21" width="46" height="20" rx="3"/>
      <text class="step-tag-text" x="51" y="36" font-size="12">Step 1</text>
      <rect class="step-tag" x="123" y="21" width="46" height="20" rx="3"/>
      <text class="step-tag-text" x="146" y="36" font-size="12">Step 2</text>
      <circle class="step-art" cx="51" cy="81" r="30" role="img" aria-label="Illustration: shaking the box of contents"/>
      <circle class="step-art" cx="146" cy="81" r="30" role="img" aria-label="Illustration: hands piercing the packet"/>
      <text class="box-text mid" font-size="9"><tspan x="51" y="125">Shake the contents</tspan><tspan x="51" y="135">to the bottom.</tspan></text>
      <text class="box-text mid" font-size="9"><tspan x="146" y="125">Pierce the packet</tspan><tspan x="146" y="135">3 to 4 times. Hands</tspan><tspan x="146" y="145">squeeze the contents out.</tspan></text>
      <rect class="step-tag" x="83" y="171" width="46" height="20" rx="3"/>
      <text class="step-tag-text" x="106" y="186" font-size="12">Step 3</text>
      <circle class="step-art" cx="106" cy="228" r="30" role="img" aria-label="Illustration: hands squeezing the contents out"/>
      <text class="box-text mid" font-size="9"><tspan x="106" y="274">Slowly squeeze the</tspan><tspan x="106" y="284">contents out.</tspan></text>
    </g>

    <!-- small three-step instructions for the counter box -->
    <g id="steps-small">
      <rect class="step-tag" x="24" y="24" width="24" height="10" rx="2"/>
      <text class="step-tag-text" x="36" y="31.5" font-size="6">Step 1</text>
      <rect class="step-tag" x="81" y="24" width="24" height="10" rx="2"/>
      <text class="step-tag-text" x="93" y="31.5" font-size="6">Step 2</text>
      <rect class="step-tag" x="137" y="24" width="24" height="10" rx="2"/>
      <text class="step-tag-text" x="149" y="31.5" font-size="6">Step 3</text>
      <circle class="step-art" cx="36" cy="60" r="17" role="img" aria-label="Illustration: shaking the box of contents"/>
      <circle class="step-art" cx="93" cy="60" r="17" role="img" aria-label="Illustration: hands piercing the packet"/>
      <circle class="step-art" cx="149" cy="60" r="17" role="img" aria-label="Illustration: hands squeezing the contents out"/>
      <text class="box-text mid" font-size="4.6"><tspan x="36" y="86">Shake the contents</tspan><tspan x="36" y="92">to the bottom.</tspan></text>
      <text class="box-text mid" font-size="4.6"><tspan x="93" y="86">Pierce the packet</tspan><tspan x="93" y="92">3 to 4 times. Hands</tspan><tspan x="93" y="98">squeeze the contents out.</tspan></text>
      <text class="box-text mid" font-size="4.6"><tspan x="149" y="86">Slowly squeeze the</tspan><tspan x="149" y="92">contents out.</tspan></text>
    </g>

    <!-- carry-handle display box shell -->
    <g id="display-shell" class="die-bottom">
      <path class="panel" d="M342,1005 L390,978 Q430,925 485,923 L645,923 Q700,925 740,978 L788,1005 L740,1075 Q700,1040 645,1030 L485,1030 Q430,1040 390,1075 Z"/>
      <line class="fold" x1="485" y1="923" x2="485" y2="1030"/>
      <line class="fold" x1="645" y1="923" x2="645" y2="1030"/>
      <rect class="panel" x="82" y="955" width="208" height="45"/>
      <rect class="panel" x="82" y="1000" width="208" height="162"/>
      <rect class="panel" x="290" y="1082" width="162" height="80"/>
      <rect class="panel" x="660" y="1082" width="160" height="80"/>
      <path class="panel" d="M35,1162 L82,1162 L82,1463 L35,1463 Z"/>
      <rect class="panel" x="82" y="1162" width="208" height="301"/>
      <rect class="panel" x="290" y="1162" width="162" height="301"/>
      <rect class="panel" x="452" y="1162" width="208" height="301"/>
      <rect class="panel" x="660" y="1162" width="160" height="301"/>
      <line class="fold" x1="290" y1="1320" x2="452" y2="1320"/>
      <line class="fold" x1="290" y1="1427" x2="452" y2="1427"/>
      <path class="panel" d="M82,1463 L290,1463 L238,1545 L238,1580 L135,1580 L135,1545 Z"/>
      <rect class="panel" x="290" y="1463" width="162" height="117"/>
      <path class="panel" d="M452,1463 L660,1463 L660,1580 L607,1580 L607,1545 L505,1545 L505,1580 L452,1580 Z"/>
      <rect class="panel" x="660" y="1463" width="160" height="117"/>

      <text class="box-text" x="95" y="1013" font-size="7" font-weight="400">U.S.A &amp; Canada</text>
      <text class="box-text end" x="282" y="1013" font-size="7" font-weight="400">European</text>
      <rect class="code-slot" x="92" y="1016" width="51" height="37" aria-label="Barcode area, U.S.A and Canada"/>
      <rect class="code-slot" x="229" y="1016" width="52" height="37" aria-label="Barcode area, European"/>
      <g class="box-text" font-size="5.2">
        <circle cx="98" cy="1068" r="2.6"/><text x="104" y="1069">SO SIMPLE TO USE EVEN A</text><text x="104" y="1075">CHILD CAN DO IT.</text>
        <circle cx="98" cy="1084" r="2.6"/><text x="104" y="1085">DON'T PUT THE CONDIMENT</text><text x="104" y="1091">PACKET IN YOUR MOUTH TO</text><text x="104" y="1097">OPEN IT.</text>
        <circle cx="98" cy="1106" r="2.6"/><text x="104" y="1107">THAT'S JUST GROSS.</text>
        <circle cx="192" cy="1068" r="2.6"/><text x="198" y="1069">USE OUR SAUCE SACHET</text><text x="198" y="1075">SNIPPER.</text>
        <circle cx="192" cy="1084" r="2.6"/><text x="198" y="1085">GREAT FOR PEOPLE ON THE GO.</text>
        <circle cx="192" cy="1093" r="2.6"/><text x="198" y="1094">DISHWASHER SAFE.</text>
        <circle cx="192" cy="1102" r="2.6"/><text x="198" y="1103">THE SAUCE SACHET SNIPPER.</text>
      </g>
      <text class="box-text mid" x="232" y="1122" font-size="6">MADE IN CHINA</text>
      <rect x="180" y="1128" width="104" height="9" fill="none" stroke="#111" stroke-width="0.8"/>
      <text class="box-text mid" x="232" y="1134.5" font-size="4" textLength="98" lengthAdjust="spacingAndGlyphs">NOT A CHILDS TOY. KEEP AWAY FROM SMALL CHILDREN.</text>
      <text class="box-text mid" x="232" y="1145" font-size="4.6">THE SAUCE SACHET SNIPPER</text>

      <use xlink:href="#steps-large" x="82" y="1162"/>
      <use xlink:href="#steps-large" x="452" y="1164"/>
    </g>
  </defs>

  <!-- counter box dieline -->
  <g class="die-top">
    <path class="panel" d="M55,150 L55,42 Q55,30 67,30 L221,30 Q233,30 233,42 L233,150 Z"/>
    <rect class="panel" x="52" y="148" width="185" height="244"/>
    <line class="fold-orange" x1="52" y1="268" x2="237" y2="268"/>
    <path d="M70,268 A73,73 0 0 0 217,268" fill="none" stroke="#555" stroke-width="1"/>
    <path class="panel" d="M262,330 L462,330 L478,380 L480,392 L237,392 L245,380 Z"/>
    <path class="panel" d="M680,330 L888,330 L905,390 L907,392 L663,392 Z"/>
    <path class="panel" d="M22,405 L52,392 L52,513 L22,500 Z"/>
    <rect class="panel" x="52" y="392" width="185" height="121"/>
    <rect class="panel" x="237" y="392" width="243" height="121"/>
    <rect class="panel" x="480" y="392" width="183" height="121"/>
    <rect class="panel" x="663" y="392" width="244" height="121"/>
    <path class="panel" d="M55,513 L235,513 L145,572 L145,610 L130,630 L55,630 Z"/>
    <path class="panel" d="M237,513 L478,513 L478,630 L420,630 L420,604 L295,604 L295,630 L237,630 Z"/>
    <path class="panel" d="M480,513 L663,513 L663,630 L580,630 L568,610 L568,572 Z"/>
    <path class="panel" d="M663,513 L907,513 L850,600 L845,630 L730,630 L723,605 Z"/>

    <text class="box-text" x="66" y="158" font-size="5.5" font-weight="400">U.S.A &amp; CANADA</text>
    <text class="box-text" x="183" y="158" font-size="5.5" font-weight="400">EUROPEAN</text>
    <rect class="code-slot" x="63" y="160" width="52" height="37" aria-label="Barcode area, U.S.A and Canada"/>
    <rect class="code-slot" x="172" y="160" width="50" height="37" aria-label="Barcode area, European"/>
    <g class="box-text" font-size="4.2">
      <circle cx="65" cy="209" r="1.8"/><text x="69" y="210.5">SO SIMPLE TO USE EVEN A CHILD CAN DO IT</text>
      <circle cx="65" cy="215.5" r="1.8"/><text x="69" y="217">DON'T PUT THE CONDIMENT PACKET IN YOUR MOUTH TO OPEN IT.</text>
      <circle cx="65" cy="222" r="1.8"/><text x="69" y="223.5">THAT'S JUST GROSS.</text>
      <circle cx="65" cy="228.5" r="1.8"/><text x="69" y="230">USE OUR SAUCE SACHET SNIPPER.</text>
      <circle cx="65" cy="235" r="1.8"/><text x="69" y="236.5">FOR PEOPLE ON THE GO.</text>
      <circle cx="65" cy="241.5" r="1.8"/><text x="69" y="243">DISHWASHER SAFE.</text>
    </g>
    <text class="box-text mid" x="168" y="242" font-size="4.4">MADE IN CHINA</text>
    <rect x="137" y="245" width="63" height="13" fill="none" stroke="#111" stroke-width="0.7"/>
    <text class="box-text mid" x="168" y="250" font-size="3.4">NOT A CHILDS TOY.</text>
    <text class="box-text mid" x="168" y="255" font-size="3.4">KEEP AWAY FROM SMALL CHILDREN.</text>

    <use xlink:href="#steps-small" x="52" y="392"/>
    <use xlink:href="#steps-small" x="480" y="397"/>

    <text class="box-text mid" font-size="6.2"><tspan x="784" y="455">Product of Norvale Goods Inc</tspan><tspan x="784" y="466">www.norvalegoods.com</tspan><tspan x="784" y="477">Product Box Code 1005</tspan></text>
    <circle class="mark-ring" cx="773" cy="489" r="7"/><text class="box-text mid" x="773" y="491.5" font-size="6" font-weight="400">TM</text>
    <circle class="mark-ring" cx="795" cy="489" r="7"/><text class="box-text mid" x="795" y="491.5" font-size="6" font-weight="400">C</text>
  </g>

  <!-- counter box dimensions -->
  <g class="dim-green">
    <line x1="980" y1="30" x2="1195" y2="30"/>
    <line x1="980" y1="628" x2="1195" y2="628"/>
    <line x1="1123" y1="30" x2="1123" y2="268"/>
    <line x1="1123" y1="390" x2="1123" y2="628"/>
    <path d="M1105,100 Q1120,70 1123,30 Q1126,70 1141,100"/>
    <path d="M1105,558 Q1120,588 1123,628 Q1126,588 1141,558"/>
    <line x1="22" y1="700" x2="22" y2="915"/>
    <line x1="907" y1="700" x2="907" y2="915"/>
    <line x1="22" y1="845" x2="345" y2="845"/>
    <line x1="585" y1="845" x2="907" y2="845"/>
    <path d="M95,827 Q62,842 22,845 Q62,848 95,863"/>
    <path d="M834,827 Q867,842 907,845 Q867,848 834,863"/>
  </g>
  <text class="dim-sans" x="1105" y="366" font-size="108">490.5</text>
  <text class="dim-sans" x="468" y="880" font-size="108">724</text>
  <text class="dim-sans" x="1025" y="815" font-size="130">E</text>

  <!-- header card: inventory codes -->
  <g class="header-card">
    <rect class="panel" x="1296" y="100" width="347" height="638"/>
    <path class="punch-frame" d="M1370,143 L1457,143 A12,12 0 0 1 1481,143 L1568,143 L1568,167 L1370,167 Z"/>
    <text class="card-text mid" x="1469" y="161" font-size="13">PUNCH OUT HOLE.</text>
    <text class="card-text mid" x="1469" y="210" font-size="21">Inventory Control Bar Codes</text>
    <rect class="pill" x="1433" y="238" width="198" height="66" rx="33"/>
    <rect class="pill" x="1433" y="338" width="198" height="66" rx="33"/>
    <rect class="pill" x="1433" y="437" width="198" height="66" rx="33"/>
    <rect class="pill" x="1433" y="537" width="198" height="66" rx="33"/>
    <rect class="code-slot" x="1310" y="262" width="112" height="93" aria-label="Barcode area, U.S.A and Canada"/>
    <rect class="code-slot" x="1310" y="462" width="112" height="93" aria-label="Barcode area, European"/>
    <text class="card-text mid" x="1366" y="381" font-size="12">U.S.A &amp; CANADA</text>
    <text class="card-text mid" x="1366" y="579" font-size="12">EUROPEAN</text>
    <text class="card-text mid" font-size="15"><tspan x="1469" y="640">Product of Norvale Goods Inc</tspan><tspan x="1469" y="658">Product # 1004</tspan><tspan x="1469" y="676">www.norvalegoods.com</tspan></text>
    <circle class="mark-ring" cx="1452" cy="696" r="12" stroke-width="1.8"/><text class="card-text mid" x="1452" y="701" font-size="12">TM</text>
    <circle class="mark-ring" cx="1488" cy="696" r="12" stroke-width="1.8"/><text class="card-text mid" x="1488" y="701" font-size="12">C</text>
    <text class="card-text mid" x="1469" y="728" font-size="11.5">Not a child's toy, keep away from small children.</text>
  </g>

  <!-- header card: product claims -->
  <g class="header-card">
    <rect class="panel" x="1668" y="100" width="347" height="638"/>
    <path class="punch-frame" d="M1743,143 L1830,143 A12,12 0 0 1 1854,143 L1941,143 L1941,167 L1743,167 Z"/>
    <text class="card-text mid" x="1842" y="160" font-size="13">PUNCH OUT HOLE.</text>
    <rect class="code-slot" x="1688" y="185" width="96" height="67" aria-label="Barcode area, U.S.A and Canada"/>
    <rect class="code-slot" x="1892" y="185" width="93" height="67" aria-label="Barcode area, European"/>
    <text class="card-text card-bold mid" font-size="14"><tspan x="1838" y="213">The sauce</tspan><tspan x="1838" y="230">sachet snipper</tspan></text>
    <text class="card-text mid" x="1736" y="271" font-size="14">U.S.A &amp; Canada</text>
    <text class="card-text mid" x="1940" y="271" font-size="14">European</text>
    <text class="card-text" font-size="21">
      <tspan x="1683" y="312">So simple</tspan><tspan x="1683" y="338">to use even</tspan><tspan x="1683" y="364">a child can</tspan><tspan x="1683" y="390">do it.</tspan>
      <tspan x="1683" y="426">Don't put the</tspan><tspan x="1683" y="452">condiment</tspan><tspan x="1683" y="478">packet in</tspan><tspan x="1683" y="504">your mouth</tspan><tspan x="1683" y="530">to open it.</tspan>
      <tspan x="1683" y="562">That's just</tspan><tspan x="1683" y="586">gross.</tspan>
      <tspan x="1683" y="610">Use our</tspan><tspan x="1683" y="634">Sauce Sachet</tspan><tspan x="1683" y="658">Snipper.</tspan>
    </text>
    <g>
      <rect class="pill" x="1811" y="288" width="198" height="66" rx="33"/><circle class="pill-dot" cx="1833" cy="321" r="9"/>
      <text class="pill-text"><tspan x="1915" y="317">The Sauce</tspan><tspan x="1915" y="335">Sachet Snipper.</tspan></text>
      <rect class="pill" x="1811" y="388" width="198" height="66" rx="33"/><circle class="pill-dot" cx="1833" cy="421" r="9"/>
      <text class="pill-text"><tspan x="1917" y="418">The Sauce</tspan><tspan x="1917" y="436">Sachet Snipper.</tspan></text>
      <rect class="pill" x="1811" y="482" width="198" height="66" rx="33"/><circle class="pill-dot" cx="1833" cy="515" r="9"/>
      <text class="pill-text"><tspan x="1917" y="512">The Sauce</tspan><tspan x="1917" y="530">Sachet Snipper.</tspan></text>
      <rect class="pill" x="1811" y="582" width="198" height="66" rx="33"/><circle class="pill-dot" cx="1839" cy="615" r="9"/>
      <text class="pill-text"><tspan x="1921" y="612">The Sauce</tspan><tspan x="1921" y="630">Sachet Snipper.</tspan></text>
    </g>
    <text class="card-text" x="1683" y="700" font-size="18">Made in China</text>
    <text class="card-text end" x="2000" y="700" font-size="18">Dishwasher safe.</text>
    <text class="card-text mid" x="1841" y="724" font-size="13.5">Not a child's toy, keep away from small children.</text>
  </g>

  <!-- display box, product 1002 -->
  <use xlink:href="#display-shell"/>
  <g class="info-panel">
    <text class="box-text mid" x="740" y="1181" font-size="10" font-weight="400">Inventory Control Bar Codes</text>
    <text class="box-text mid" x="740" y="1203" font-size="10" font-weight="400">U.S.A &amp; Canada</text>
    <rect class="code-slot" x="693" y="1208" width="92" height="68" aria-label="Barcode area, U.S.A and Canada"/>
    <text class="box-text mid" x="740" y="1303" font-size="10" font-weight="400">European</text>
    <rect class="code-slot" x="693" y="1308" width="92" height="72" aria-label="Barcode area, European"/>
    <text class="box-text mid" font-size="9"><tspan x="740" y="1401">Product of Norvale Goods Inc</tspan><tspan x="740" y="1413">www.norvalegoods.com</tspan><tspan x="740" y="1425">Product # 1002</tspan></text>
    <circle class="mark-ring" cx="727" cy="1440" r="8"/><text class="box-text mid" x="727" y="1443" font-size="7" font-weight="400">TM</text>
    <circle class="mark-ring" cx="751" cy="1440" r="8"/><text class="box-text mid" x="751" y="1443" font-size="7" font-weight="400">C</text>
  </g>
  <g class="dim-blue">
    <line x1="932" y1="923" x2="1020" y2="923"/>
    <line x1="932" y1="1580" x2="1020" y2="1580"/>
    <line x1="975" y1="923" x2="975" y2="1220"/>
    <line x1="975" y1="1290" x2="975" y2="1580"/>
    <path d="M965,968 Q973,945 975,923 Q977,945 985,968"/>
    <path d="M965,1535 Q973,1558 975,1580 Q977,1558 985,1535"/>
    <line x1="35" y1="1625" x2="35" y2="1710"/>
    <line x1="820" y1="1625" x2="820" y2="1710"/>
    <line x1="35" y1="1668" x2="290" y2="1668"/>
    <line x1="567" y1="1668" x2="820" y2="1668"/>
    <path d="M80,1658 Q57,1666 35,1668 Q57,1670 80,1678"/>
    <path d="M775,1658 Q798,1666 820,1668 Q798,1670 775,1678"/>
  </g>
  <text class="dim-serif" x="945" y="1276" font-size="62">352.76</text>
  <text class="dim-serif" x="397" y="1714" font-size="62">420.60</text>

  <!-- display box, product 1001 -->
  <use xlink:href="#display-shell" transform="translate(1062,923) scale(0.958) translate(-35,-923)"/>
  <circle cx="1174" cy="1130" r="17" fill="var(--ink)"/>
  <g class="info-panel">
    <text class="box-text mid" x="1737" y="1171" font-size="9.5" font-weight="400">Inventory Control Bar Codes</text>
    <text class="box-text mid" x="1737" y="1190" font-size="7" font-weight="400">U.S.A &amp; CANADA</text>
    <rect class="code-slot" x="1693" y="1195" width="87" height="62" aria-label="Barcode area, U.S.A and Canada"/>
    <text class="box-text mid" x="1737" y="1278" font-size="7" font-weight="400">EUROPEAN</text>
    <rect class="code-slot" x="1693" y="1284" width="87" height="63" aria-label="Barcode area, European"/>
    <text class="box-text mid" font-size="8.6"><tspan x="1737" y="1367">Product of Norvale Goods Inc</tspan><tspan x="1737" y="1380">www.norvalegoods.com</tspan><tspan x="1737" y="1393">Product # 1001</tspan><tspan x="1737" y="1406">Count 24</tspan></text>
    <circle class="mark-ring" cx="1725" cy="1423" r="8"/><text class="box-text mid" x="1725" y="1426" font-size="7" font-weight="400">TM</text>
    <circle class="mark-ring" cx="1750" cy="1423" r="8"/><text class="box-text mid" x="1750" y="1426" font-size="7" font-weight="400">C</text>
  </g>
  <g class="dim-blue">
    <line x1="1920" y1="923" x2="2005" y2="923"/>
    <line x1="1920" y1="1553" x2="2005" y2="1553"/>
    <line x1="1963" y1="923" x2="1963" y2="1205"/>
    <line x1="1963" y1="1275" x2="1963" y2="1553"/>
    <path d="M1953,968 Q1961,945 1963,923 Q1965,945 1973,968"/>
    <path d="M1953,1508 Q1961,1531 1963,1553 Q1965,1531 1973,1508"/>
    <line x1="1062" y1="1595" x2="1062" y2="1680"/>
    <line x1="1814" y1="1595" x2="1814" y2="1680"/>
    <line x1="1062" y1="1637" x2="1305" y2="1637"/>
    <line x1="1572" y1="1637" x2="1814" y2="1637"/>
    <path d="M1107,1627 Q1084,1635 1062,1637 Q1084,1639 1107,1647"/>
    <path d="M1769,1627 Q1792,1635 1814,1637 Q1792,1639 1769,1647"/>
  </g>
  <text class="dim-serif" x="1935" y="1262" font-size="62">352.76</text>
  <text class="dim-serif" x="1410" y="1682" font-size="62">420.60</text>
</svg>
</body>
</html>
```